KAV cards & more
Business cards, fax cover sheet, letterhead, envelopes, powerpoint slide template
Modern
Tad Willers
Owner
17 Lindgate Row Tessbury, KS 66215
twkav@mailvane.net
Please integrate my already-completed company logo (attached) in a clean, modern design for business cards, Fax cover sheet, letterhead, envelopes, and powerpoint slide template

```html
<!DOCTYPE html>
<html lang="en">
<head>
<meta charset="utf-8">
<title>KAV stationery set</title>
<link href="https://fonts.googleapis.com/css2?family=Orbitron:wght@700&family=Arimo:wght@400;700&display=swap" rel="stylesheet">
<style>
:root{
  --black:#0b0b0b;
  --green:#2e9a2a;
  --lime:#b7d21c;
  --yellow:#e4e41a;
  --paper:#ffffff;
  --line:#9a9a9a;
  --text:#333333;
  --faint:#e7f0e4;
}
*{box-sizing:border-box;margin:0;padding:0}
html,body{width:1200px;height:540px;overflow:hidden;background:#fff;font-family:Arimo,Arial,sans-serif;color:var(--text)}
.stage{position:relative;width:1200px;height:540px}
.set-label{position:absolute;left:29px;top:12px;font:400 18px "Times New Roman",serif;color:#000}
.sheet{position:absolute;background:var(--paper);box-shadow:0 0 3px rgba(0,0,0,.35);overflow:hidden}
.fax{left:29px;top:43px;width:367px;height:461px}
.letterhead{left:420px;top:43px;width:372px;height:461px}
.header{position:absolute;left:0;top:0;width:100%;height:48px;background:linear-gradient(90deg,var(--black) 0%,var(--black) 72%,#1c4d14 84%,var(--green) 92%,var(--lime) 100%)}
.header::after{content:"";position:absolute;left:0;bottom:-4px;width:100%;height:4px;background:linear-gradient(90deg,var(--green),var(--lime) 60%,var(--yellow))}
.brand{position:absolute;left:12px;top:8px;display:flex;align-items:center;gap:6px}
.brand-dot{width:24px;height:24px;border-radius:50%;background:var(--green)}
.brand-name{font:700 20px Orbitron,Arimo,sans-serif;color:var(--green);letter-spacing:1px;line-height:1}
.tagline{position:absolute;left:42px;top:34px;font-size:5px;color:#ccc}
.head-contact{position:absolute;left:150px;top:10px;font-size:5.5px;line-height:8px;color:#ddd}
.footer-bar{position:absolute;left:0;bottom:0;width:100%;height:6px;background:linear-gradient(90deg,var(--green),var(--lime) 55%,var(--yellow))}
.fax-fields{position:absolute;left:26px;top:78px;display:grid;grid-template-columns:1fr 1fr;column-gap:26px;row-gap:9px;width:320px}
.field{display:flex;align-items:flex-end;font-size:7px;gap:4px}
.field span{width:26px}
.field i{flex:1;border-bottom:1px solid var(--line);height:8px}
.checks{position:absolute;left:26px;top:152px;display:flex;gap:12px;font-size:6.5px}
.checks label{display:flex;align-items:center;gap:3px}
.checks b{width:7px;height:7px;border:1px solid #555;display:inline-block}
.foot-contact{position:absolute;left:18px;bottom:16px;font-size:5.5px;line-height:8px;color:#555}
.watermark{position:absolute;border-radius:50%;background:var(--faint)}
.card{position:absolute;top:144px;width:134px;height:74px;box-shadow:0 0 3px rgba(0,0,0,.35);overflow:hidden}
.card-front{left:821px;background:#fff}
.card-front .brand{left:6px;top:6px;gap:3px}
.card-front .brand-dot{width:10px;height:10px}
.card-front .brand-name{font-size:9px}
.person{position:absolute;right:8px;top:10px;font-size:5.5px;text-align:right;color:#333}
.card-contact{position:absolute;left:6px;top:28px;font-size:4.5px;line-height:6.5px;color:#444}
.card-front .footer-bar{height:4px}
.card-back{left:1003px;background:var(--black);display:flex;align-items:center;justify-content:center}
.card-back .emblem{width:52px;height:52px;border-radius:50%;background:var(--green);display:flex;align-items:center;justify-content:center;font:700 14px Orbitron,Arimo,sans-serif;color:var(--black)}
.envelope{position:absolute;left:792px;top:300px;width:396px;height:194px;background:#fff;box-shadow:0 0 3px rgba(0,0,0,.35);overflow:hidden}
.flap{position:absolute;left:0;top:0;width:100%;height:34px;background:var(--black)}
.envelope .brand{top:42px}
.envelope .tagline{top:66px}
.envelope .footer-bar{height:5px}
</style>
</head>
<body>
<div class="stage">
  <div class="set-label">FAX</div>

  <section class="sheet fax">
    <header class="header">
      <div class="brand"><span class="brand-dot"></span><span class="brand-name">KAV</span></div>
      <div class="tagline">Cards and Print Studio</div>
      <div class="head-contact">17 Lindgate Row Tessbury, KS 66215<br>Tel 555 310 0142<br>twkav@mailvane.net</div>
    </header>
    <div class="fax-fields">
      <div class="field"><span>To:</span><i></i></div><div class="field"><span>From:</span><i></i></div>
      <div class="field"><span>Fax:</span><i></i></div><div class="field"><span>Pages:</span><i></i></div>
      <div class="field"><span>Phone:</span><i></i></div><div class="field"><span>Date:</span><i></i></div>
      <div class="field"><span>Re:</span><i></i></div><div class="field"><span>CC:</span><i></i></div>
    </div>
    <div class="checks">
      <label><b></b>Urgent</label><label><b></b>For Review</label><label><b></b>Please Comment</label><label><b></b>Please Reply</label><label><b></b>Please Recycle</label>
    </div>
    <div class="footer-bar"></div>
  </section>

  <section class="sheet letterhead">
    <header class="header">
      <div class="brand"><span class="brand-dot"></span><span class="brand-name">KAV</span></div>
      <div class="tagline">Cards and Print Studio</div>
      <div class="head-contact">17 Lindgate Row Tessbury, KS 66215<br>Tel 555 310 0142<br>twkav@mailvane.net</div>
    </header>
    <div class="watermark" style="right:-10px;bottom:20px;width:110px;height:110px"></div>
    <div class="foot-contact">17 Lindgate Row Tessbury, KS 66215<br>Tel 555 310 0142<br>twkav@mailvane.net</div>
    <div class="footer-bar"></div>
  </section>

  <div class="card card-front">
    <div class="brand"><span class="brand-dot"></span><span class="brand-name">KAV</span></div>
    <div class="person"><strong>Tad Willers</strong><br>Owner</div>
    <div class="card-contact">17 Lindgate Row<br>Tessbury, KS 66215<br>twkav@mailvane.net</div>
    <div class="footer-bar"></div>
  </div>
  <div class="card card-back"><div class="emblem">KAV</div></div>

  <section class="envelope">
    <div class="flap"></div>
    <div class="brand"><span class="brand-dot"></span><span class="brand-name">KAV</span></div>
    <div class="tagline">Cards and Print Studio</div>
    <div class="watermark" style="right:12px;bottom:14px;width:80px;height:80px"></div>
    <div class="foot-contact" style="left:12px;bottom:14px">17 Lindgate Row Tessbury, KS 66215<br>twkav@mailvane.net</div>
    <div class="footer-bar"></div>
  </section>
</div>
</body>
</html>
```